Book Title: “Harbor: Road of Quiet Mercy” Please see the attachment “Text on the cover”.

Book Cover Design Instructions: This book is meant for people of all religions and nationalities. Therefore, on the cover, there should be no mosque or an object specific to any religion. The primary emphasis should be on the "unconditional love of God." Therefore, use universal symbols of love. The second priority themes could be Sufism, Peace, and self-improvement. Rest is your imagination. Please also see the attachment: 'Book description and author's Bio.'
This book has the potential to be a best seller. Please do a good job.
What Book Cover Formats are required: A designer should submit cover designs in three formats: (1) eBook, (2) Paperback, and (3) Hardback. These books will be published on Veltrano PBX.
Format requirements for eBooks are available from: https://pub.veltrano.example/en_US/help/topic/K481207735.
You can find paperback and hardback cover measurements from: https://pub.veltrano.example/en_US/cover-calculator
• To complete the project, all three formats should be accepted by Veltrano PBX.
• The book interior trim size is 6.14 X 9.21 inches.
• Interior Type: Premium color.
• No bleed.
• I do not upload barcode. So, the back cover should have room for Veltrano to print the barcode.
• Number of pages 126.
Compensation for the designer: After selecting one designer, I will increase the amount by $200 on Brushmarket to compensate for three deliverables.
Follow-up of the Project:
After the book is published, I may need minor revisions. For example, the number of pages may change. Therefore, I will need the same design in revised sizes. In that case, I will pay $25 for each revision. For example, if the number of pages changes, I will need a different spine for paperback and hardback, then I will pay the artist $25 + $25 = $50 for both designs.
List of Enclosers:
1. Text on the cover.
2. Book description and author's Bio for the back cover.
3. Later, I will upload my picture for the book's back cover.

Target Market(s)

Any adult

Industry/Entity Type

Any industry

Requirements
Must have
• Three Deliverables

```html
<!DOCTYPE html>
<html lang="en">
<head>
<meta charset="utf-8">
<title>Harbor: Road of Quiet Mercy — Cover</title>
<link rel="stylesheet" href="https://fonts.googleapis.com/css2?family=Bebas+Neue&family=Montserrat:wght@500;600;700&display=swap">
<style>
  :root {
    --navy: #1c1760;
    --yellow: #ffe800;
    --band-ink: #1c1796;
    --white: #ffffff;
    --page: #ffffff;
  }
  html, body {
    margin: 0;
    padding: 0;
    width: 1200px;
    height: 1200px;
    overflow: hidden;
    background: var(--page);
  }
  .canvas {
    position: relative;
    width: 1200px;
    height: 1200px;
  }
  .book-cover {
    position: absolute;
    left: 293px;
    top: 140px;
    width: 614px;
    height: 920px;
    display: block;
  }
  .cover-bg { fill: var(--navy); }
  .title-band { fill: var(--yellow); }
  .kicker {
    font-family: "Montserrat", sans-serif;
    font-weight: 500;
    font-size: 25px;
    fill: var(--white);
  }
  .title-condensed {
    font-family: "Bebas Neue", sans-serif;
    font-weight: 400;
  }
  .title-white { fill: var(--white); }
  .title-yellow { fill: var(--yellow); }
  .title-band-word {
    font-family: "Montserrat", sans-serif;
    font-weight: 700;
    font-size: 187px;
    fill: var(--band-ink);
  }
  .subtitle {
    font-family: "Montserrat", sans-serif;
    font-weight: 600;
    font-size: 31px;
    fill: var(--white);
  }
  .subtitle .accent { fill: var(--yellow); }
  .author {
    font-family: "Montserrat", sans-serif;
    font-weight: 600;
    font-size: 31px;
    fill: var(--white);
  }
</style>
</head>
<body>
<div class="canvas">
  <svg class="book-cover" viewBox="0 0 614 920" xmlns="http://www.w3.org/2000/svg" aria-label="Book cover: Harbor: Road of Quiet Mercy">
    <defs>
      <linearGradient id="rule-fade" x1="0" x2="1" y1="0" y2="0">
        <stop offset="0" stop-color="#ffffff" stop-opacity="0"/>
        <stop offset="0.5" stop-color="#ffffff" stop-opacity="0.75"/>
        <stop offset="1" stop-color="#ffffff" stop-opacity="0"/>
      </linearGradient>
    </defs>

    <rect class="cover-bg" x="0" y="0" width="614" height="920"/>

    <text class="kicker" x="307" y="41" text-anchor="middle" textLength="449" lengthAdjust="spacingAndGlyphs">UNCONDITIONAL LOVE OF GOD</text>

    <text class="title-condensed title-white" x="307" y="197" font-size="187" text-anchor="middle" textLength="420" lengthAdjust="spacingAndGlyphs">HARBOR</text>
    <text class="title-condensed title-yellow" x="307" y="369" font-size="212" text-anchor="middle" textLength="525" lengthAdjust="spacingAndGlyphs">ROAD OF</text>
    <text class="title-condensed title-yellow" x="307" y="544" font-size="210" text-anchor="middle" textLength="525" lengthAdjust="spacing">QUIET</text>

    <rect class="title-band" x="0" y="580" width="614" height="173"/>
    <text class="title-band-word" x="307" y="734" text-anchor="middle" textLength="530" lengthAdjust="spacingAndGlyphs">MERCY</text>

    <rect x="140" y="772" width="350" height="1.5" fill="url(#rule-fade)"/>
    <text class="subtitle" x="307" y="809" text-anchor="middle" textLength="526" lengthAdjust="spacingAndGlyphs">GUIDE TO CULTIVATING INNER</text>
    <text class="subtitle" x="307" y="846" text-anchor="middle" textLength="492" lengthAdjust="spacingAndGlyphs">PEACE <tspan class="accent">AND MINDFUL LIVING</tspan></text>
    <rect x="140" y="856" width="350" height="1.5" fill="url(#rule-fade)"/>

    <text class="author" x="307" y="900" text-anchor="middle" textLength="346" lengthAdjust="spacingAndGlyphs">DR. IREM VALDANI</text>
  </svg>
</div>
</body>
</html>
```